Quillmere Ripple alcohol cooler

I need a design using my Quillmere Beverage Logo for 4 different styles of Malt Beverage. The cocktails are easy drinking tropical feel. We will be using the best ingredients and try to be all natural and organic.
Tovel Lime
Tovel Orange
Tovel Grapefruit
Tovel Strawberry
We would like as few colors as possible in the design.

Target Market(s)

21 - 50
Women

Requirements
Must have
• the 4 styles
• my LOGO
• label dimension inside 3"wide x 4"high maximum
• 4 pack design
• label must have 12 FL OZ
• label must have 5% ALC/VOL
Nice to have
• Clean crisp feel
Should not have
• please keep design to 3 colors or less

```html
<!DOCTYPE html>
<html lang="en">
<head>
<meta charset="utf-8">
<title>Quillmere Ripple – Tovel Labels</title>
<link rel="stylesheet" href="https://fonts.googleapis.com/css2?family=Bree+Serif&family=Raleway:wght@400;600&display=swap">
<style>
  :root {
    --backdrop: #201e1f;
    --paper: #ffffff;
    --brand-green: #35654b;
    --ink: #3a3a3a;
  }
  html, body {
    margin: 0;
    width: 966px;
    height: 1200px;
    overflow: hidden;
    background: var(--backdrop);
  }
  .sheet {
    position: relative;
    width: 966px;
    height: 1200px;
  }
  .label {
    position: absolute;
    width: 351px;
    height: 468px;
    background: var(--paper);
  }
  .label--lime { left: 125px; top: 125px; }
  .label--orange { left: 490px; top: 125px; }
  .label--grapefruit { left: 125px; top: 607px; }
  .label--strawberry { left: 490px; top: 607px; }
  .label svg { display: block; width: 351px; height: 468px; }
  .brand-name {
    font-family: "Raleway", sans-serif;
    font-weight: 600;
    fill: var(--brand-green);
    font-size: 26px;
    letter-spacing: 3px;
  }
  .brand-dot { fill: var(--brand-green); }
  .flavour-name {
    font-family: "Bree Serif", serif;
    fill: var(--paper);
    stroke: var(--brand-green);
    stroke-width: 6px;
    paint-order: stroke fill;
    stroke-linejoin: round;
  }
  .spec {
    font-family: "Raleway", sans-serif;
    font-weight: 400;
    font-size: 16px;
    fill: var(--ink);
  }
</style>
</head>
<body>
<main class="sheet">

  <section class="label label--lime">
    <svg viewBox="0 0 439 585" aria-label="Tovel Lime label">
      <defs>
        <linearGradient id="lime-band" x1="0" y1="1" x2="1" y2="0">
          <stop offset="0" stop-color="#a3e22b"/><stop offset=".35" stop-color="#5ed138"/><stop offset=".75" stop-color="#00b544"/><stop offset="1" stop-color="#00aa45"/>
        </linearGradient>
      </defs>
      <circle class="brand-dot" cx="219.5" cy="112" r="14"/>
      <text class="brand-name" x="219.5" y="167" text-anchor="middle">QUILLMERE</text>
      <text class="brand-name" x="219.5" y="201" text-anchor="middle">BEVERAGE</text>
      <polygon points="0,332 175,351 0,368" fill="#12ad4f"/>
      <polygon points="0,375 439,332 439,482 0,527" fill="url(#lime-band)"/>
      <polygon points="264,506 439,491 439,527" fill="#cfe03a"/>
      <g transform="rotate(-5 220 450)">
        <text class="flavour-name" x="220" y="428" text-anchor="middle" font-size="74">Tovel</text>
        <text class="flavour-name" x="220" y="492" text-anchor="middle" font-size="72">Lime</text>
      </g>
      <text class="spec" x="36" y="552">5% ALC/VOL</text>
      <text class="spec" x="395" y="552" text-anchor="end">12 FL OZ.</text>
    </svg>
  </section>

  <section class="label label--orange">
    <svg viewBox="0 0 439 585" aria-label="Tovel Orange label">
      <defs>
        <linearGradient id="orange-band" x1="0" y1="1" x2="1" y2="0">
          <stop offset="0" stop-color="#f7941d"/><stop offset=".4" stop-color="#fbac18"/><stop offset=".75" stop-color="#f7941d"/><stop offset="1" stop-color="#f26a21"/>
        </linearGradient>
      </defs>
      <circle class="brand-dot" cx="219.5" cy="112" r="14"/>
      <text class="brand-name" x="219.5" y="167" text-anchor="middle">QUILLMERE</text>
      <text class="brand-name" x="219.5" y="201" text-anchor="middle">BEVERAGE</text>
      <polygon points="0,332 175,351 0,368" fill="#f07e3b"/>
      <polygon points="0,375 439,332 439,482 0,527" fill="url(#orange-band)"/>
      <polygon points="264,506 439,491 439,527" fill="#ffd22e"/>
      <g transform="rotate(-5 220 450)">
        <text class="flavour-name" x="220" y="428" text-anchor="middle" font-size="74">Tovel</text>
        <text class="flavour-name" x="220" y="492" text-anchor="middle" font-size="72">Orange</text>
      </g>
      <text class="spec" x="36" y="552">5% ALC/VOL</text>
      <text class="spec" x="395" y="552" text-anchor="end">12 FL OZ.</text>
    </svg>
  </section>

  <section class="label label--grapefruit">
    <svg viewBox="0 0 439 585" aria-label="Tovel Grapefruit label">
      <defs>
        <linearGradient id="grapefruit-band" x1="0" y1="1" x2="1" y2="0">
          <stop offset="0" stop-color="#f99d1c"/><stop offset=".45" stop-color="#f7941d"/><stop offset=".8" stop-color="#f15a22"/><stop offset="1" stop-color="#ee3424"/>
        </linearGradient>
      </defs>
      <circle class="brand-dot" cx="219.5" cy="112" r="14"/>
      <text class="brand-name" x="219.5" y="167" text-anchor="middle">QUILLMERE</text>
      <text class="brand-name" x="219.5" y="201" text-anchor="middle">BEVERAGE</text>
      <polygon points="0,332 175,351 0,368" fill="#ea4335"/>
      <polygon points="0,375 439,332 439,482 0,527" fill="url(#grapefruit-band)"/>
      <polygon points="264,506 439,491 439,527" fill="#fec62c"/>
      <g transform="rotate(-5 220 450)">
        <text class="flavour-name" x="220" y="428" text-anchor="middle" font-size="74">Tovel</text>
        <text class="flavour-name" x="220" y="492" text-anchor="middle" font-size="70">Grapefruit</text>
      </g>
      <text class="spec" x="36" y="552">5% ALC/VOL</text>
      <text class="spec" x="395" y="552" text-anchor="end">12 FL OZ.</text>
    </svg>
  </section>

  <section class="label label--strawberry">
    <svg viewBox="0 0 439 585" aria-label="Tovel Strawberry label">
      <defs>
        <linearGradient id="strawberry-band" x1="0" y1="1" x2="1" y2="0">
          <stop offset="0" stop-color="#e8268f"/><stop offset=".4" stop-color="#ee4a9f"/><stop offset=".8" stop-color="#e8308f"/><stop offset="1" stop-color="#e5268c"/>
        </linearGradient>
      </defs>
      <circle class="brand-dot" cx="219.5" cy="112" r="14"/>
      <text class="brand-name" x="219.5" y="167" text-anchor="middle">QUILLMERE</text>
      <text class="brand-name" x="219.5" y="201" text-anchor="middle">BEVERAGE</text>
      <polygon points="0,332 175,351 0,368" fill="#e12a88"/>
      <polygon points="0,375 439,332 439,482 0,527" fill="url(#strawberry-band)"/>
      <polygon points="264,506 439,491 439,527" fill="#ef519d"/>
      <g transform="rotate(-5 220 450)">
        <text class="flavour-name" x="220" y="428" text-anchor="middle" font-size="74">Tovel</text>
        <text class="flavour-name" x="220" y="492" text-anchor="middle" font-size="70">Strawberry</text>
      </g>
      <text class="spec" x="36" y="552">5% ALC/VOL</text>
      <text class="spec" x="395" y="552" text-anchor="end">12 FL OZ.</text>
    </svg>
  </section>

</main>
</body>
</html>
```